Velisa Seafood Shipping Packaging Re-Design

We need a packaging (Shipping Carton) design for our Seafood Products (FROZEN). We already have a basic packaging design which we prefer to have a modern touch on it.
Spec :
1. It must show our logo (Attached), note that the text of "VELISA" which accompany the logo is optional, it can be omitted & showing only the logo.
2. Main color is Blue
3. Our carton is regular shipping box with dimension L43cm x W 27cm x H 16cm.
4. Our material of Carton is both Brown & White Kraft Paperboard, so the design should look nice in both material.

Attached our Logo and packaging design.

Target Market(s)

Frozen Seafood Distributor & Seafood Buyer

Industry/Entity Type

Food Production

Requirements
Must have
• 1. Must Show our Logo
• 2. Main Color of the Text/Logo is Blue
• 3. On the side of the packaging / Carton must show two box of CODE & SIZE
• 4. Must Show these icons :
• a. Handle with Care
• b. Maximum Stackable 10 Carton
• c. Recyleable Material
• d. Protect from the Water/Rain
Nice to have
• Would prefer to have a modern design

```html
<!DOCTYPE html>
<html lang="en">
<head>
<meta charset="utf-8">
<title>Velisa Shipping Carton – Dielines</title>
<link href="https://fonts.googleapis.com/css2?family=EB+Garamond:wght@400;500&family=Open+Sans:wght@400;600&display=swap" rel="stylesheet">
<style>
  :root{
    --paper-white:#ffffff;
    --paper-kraft:#e4c690;
    --dieline:#8f8f8f;
    --navy:#2a2f72;
    --brand-blue:#1d5ea8;
    --sea-light:#cfe4f5;
    --sea-mid:#5ea3d6;
    --sea-deep:#0072b5;
    --wordmark-pale:#e3edf8;
    --wordmark-kraft:#edf3f9;
  }
  *{box-sizing:border-box;margin:0;padding:0}
  html,body{width:1186px;height:1200px;overflow:hidden;background:#fff}
  body{position:relative;font-family:"Open Sans",Arial,sans-serif}

  .sheet{position:absolute;left:0;width:1160px;height:640px;--paper:var(--paper-white)}
  .sheet--white{top:0}
  .sheet--kraft{top:538px;left:2px;--paper:var(--paper-kraft)}

  .sample-label{position:absolute;left:112px;top:134px;font:12px "EB Garamond",serif;color:#222}

  .dieline{position:absolute;left:0;top:0}
  .dieline polygon,.dieline rect{fill:var(--paper);stroke:var(--dieline);stroke-width:.8}

  .panel{position:absolute;overflow:hidden}
  .panel--front-a{left:80px;top:205px;width:392px;height:248px}
  .panel--front-c{left:617px;top:205px;width:393px;height:248px}
  .sheet--white .panel--front-a,.sheet--white .panel--front-c{
    background:linear-gradient(#fff 0%,#fff 30%,var(--sea-light) 75%,#b9d8f0 100%)}
  .sheet--kraft .panel--front-a,.sheet--kraft .panel--front-c{
    background:linear-gradient(var(--paper-kraft) 0%,#e2cfa4 40%,#c9dbe4 70%,#b6d6ef 100%)}

  .wordmark-bg{position:absolute;left:0;right:0;top:22px;text-align:center;
    font:400 72px/1 "EB Garamond",serif;letter-spacing:2px;color:var(--wordmark-pale)}
  .sheet--kraft .wordmark-bg{color:var(--wordmark-kraft)}

  .waves{position:absolute;left:0;right:0;bottom:0;height:92px;
    background:linear-gradient(#d8eaf7 0%,#8ec0e6 30%,var(--sea-mid) 55%,var(--sea-deep) 78%,var(--sea-deep) 100%)}

  .brand{position:absolute;display:flex;align-items:center;gap:8px;
    font:500 34px/1 "EB Garamond",serif;color:var(--brand-blue)}
  .brand__dot{width:18px;height:18px;border-radius:50%;background:var(--brand-blue)}
  .panel--front-a .brand,.panel--front-c .brand{left:50%;top:110px;transform:translateX(-50%)}

  .panel--bottom{left:80px;top:453px;width:392px;height:144px;display:flex;align-items:center;justify-content:center}
  .panel--top{left:617px;top:62px;width:393px;height:143px;display:flex;align-items:center;justify-content:center}
  .panel--bottom .brand,.panel--top .brand{position:static;font-size:28px}
  .name-plate{font:400 44px/1 "EB Garamond",serif;color:var(--navy);letter-spacing:1px}
  .name-plate--flipped{transform:rotate(180deg)}

  .panel--side-b{left:472px;top:205px;width:145px;height:248px}
  .panel--side-d{left:1010px;top:205px;width:145px;height:248px}
  .spec-box{position:absolute;left:27px;width:93px;height:73px;border:1.2px solid var(--navy);border-radius:7px}
  .spec-box--code{top:30px}
  .spec-box--size{top:116px}
  .spec-box__label{height:15px;border-bottom:1.2px solid var(--navy);font-size:10px;line-height:14px;padding-left:9px;color:var(--navy)}
  .care-icons{position:absolute;left:27px;top:202px;display:flex;gap:4px}
  .care-icon{width:20px;height:20px}
  .care-icon rect{fill:none;stroke:var(--navy);stroke-width:1.2}
  .care-icon .glyph{fill:var(--navy)}
  .care-icon .line{fill:none;stroke:var(--navy);stroke-width:1.3}
  .care-icon text{font:600 9px "Open Sans",sans-serif;fill:var(--navy)}
</style>
</head>
<body>

<!-- ===== White board version ===== -->
<section class="sheet sheet--white">
  <p class="sample-label">sample 1</p>
  <svg class="dieline" width="1160" height="640" viewBox="0 0 1160 640">
    <polygon points="80,205 36,240 36,420 80,453"/>
    <polygon points="80,205 108,163 442,163 472,205"/>
    <rect x="80" y="205" width="392" height="248"/>
    <rect x="80" y="453" width="392" height="144"/>
    <polygon points="80,597 108,639 442,639 472,597"/>
    <polygon points="472,205 500,163 590,163 617,205"/>
    <rect x="472" y="205" width="145" height="248"/>
    <polygon points="472,453 500,495 590,495 617,453"/>
    <polygon points="617,62 645,18 982,18 1010,62"/>
    <rect x="617" y="62" width="393" height="143"/>
    <rect x="617" y="205" width="393" height="248"/>
    <polygon points="617,453 645,495 982,495 1010,453"/>
    <rect x="1010" y="205" width="145" height="248"/>
  </svg>

  <div class="panel panel--front-a">
    <p class="wordmark-bg">VELISA</p>
    <div class="waves" role="img" aria-label="Stylized blue ocean waves"></div>
    <div class="brand"><span class="brand__dot"></span>Velisa</div>
  </div>
  <div class="panel panel--bottom"><div class="brand"><span class="brand__dot"></span>Velisa</div></div>

  <div class="panel panel--side-b">
    <div class="spec-box spec-box--code"><div class="spec-box__label">CODE/</div></div>
    <div class="spec-box spec-box--size"><div class="spec-box__label">SIZE/</div></div>
    <div class="care-icons">
      <svg class="care-icon" viewBox="0 0 20 20" aria-label="Keep dry"><rect x="1" y="1" width="18" height="18" rx="3"/><path class="glyph" d="M10 4 C13 8 14 10 14 12 A4 4 0 0 1 6 12 C6 10 7 8 10 4Z"/><path class="line" d="M5 15 L15 5"/></svg>
      <svg class="care-icon" viewBox="0 0 20 20" aria-label="Handle with care"><rect x="1" y="1" width="18" height="18" rx="3"/><circle class="glyph" cx="10" cy="7" r="2.5"/><path class="line" d="M4 10 Q5 15 10 15 Q15 15 16 10"/></svg>
      <svg class="care-icon" viewBox="0 0 20 20" aria-label="Maximum stack 10 cartons"><rect x="1" y="1" width="18" height="18" rx="3"/><text x="10" y="11" text-anchor="middle">10</text><path class="line" d="M5 13.5 H15 M5 16 H15"/></svg>
      <svg class="care-icon" viewBox="0 0 20 20" aria-label="Recyclable"><rect x="1" y="1" width="18" height="18" rx="3"/><path class="line" d="M10 4.5 L6 11 M7.5 14.5 H14 M15 11 L12 6"/><path class="glyph" d="M10 4 L12.5 5.5 L10.5 7Z M6 15 L5 12.5 L7.5 13Z M15.5 12 L13.5 14.5 L13 12Z"/></svg>
    </div>
  </div>

  <div class="panel panel--top"><div class="brand"><span class="brand__dot"></span>Velisa</div></div>
  <div class="panel panel--front-c">
    <p class="wordmark-bg">VELISA</p>
    <div class="waves" role="img" aria-label="Stylized blue ocean waves"></div>
    <div class="brand"><span class="brand__dot"></span>Velisa</div>
  </div>

  <div class="panel panel--side-d">
    <div class="spec-box spec-box--code"><div class="spec-box__label">CODE/</div></div>
    <div class="spec-box spec-box--size"><div class="spec-box__label">SIZE/</div></div>
    <div class="care-icons">
      <svg class="care-icon" viewBox="0 0 20 20" aria-label="Keep dry"><rect x="1" y="1" width="18" height="18" rx="3"/><path class="glyph" d="M10 4 C13 8 14 10 14 12 A4 4 0 0 1 6 12 C6 10 7 8 10 4Z"/><path class="line" d="M5 15 L15 5"/></svg>
      <svg class="care-icon" viewBox="0 0 20 20" aria-label="Handle with care"><rect x="1" y="1" width="18" height="18" rx="3"/><circle class="glyph" cx="10" cy="7" r="2.5"/><path class="line" d="M4 10 Q5 15 10 15 Q15 15 16 10"/></svg>
      <svg class="care-icon" viewBox="0 0 20 20" aria-label="Maximum stack 10 cartons"><rect x="1" y="1" width="18" height="18" rx="3"/><text x="10" y="11" text-anchor="middle">10</text><path class="line" d="M5 13.5 H15 M5 16 H15"/></svg>
      <svg class="care-icon" viewBox="0 0 20 20" aria-label="Recyclable"><rect x="1" y="1" width="18" height="18" rx="3"/><path class="line" d="M10 4.5 L6 11 M7.5 14.5 H14 M15 11 L12 6"/><path class="glyph" d="M10 4 L12.5 5.5 L10.5 7Z M6 15 L5 12.5 L7.5 13Z M15.5 12 L13.5 14.5 L13 12Z"/></svg>
    </div>
  </div>
</section>

<!-- ===== Kraft board version ===== -->
<section class="sheet sheet--kraft">
  <p class="sample-label">sample 2</p>
  <svg class="dieline" width="1160" height="640" viewBox="0 0 1160 640">
    <polygon points="80,205 36,240 36,420 80,453"/>
    <polygon points="80,205 108,163 442,163 472,205"/>
    <rect x="80" y="205" width="392" height="248"/>
    <rect x="80" y="453" width="392" height="144"/>
    <polygon points="80,597 108,639 442,639 472,597"/>
    <polygon points="472,205 500,163 590,163 617,205"/>
    <rect x="472" y="205" width="145" height="248"/>
    <polygon points="472,453 500,495 590,495 617,453"/>
    <polygon points="617,62 645,18 982,18 1010,62"/>
    <rect x="617" y="62" width="393" height="143"/>
    <rect x="617" y="205" width="393" height="248"/>
    <polygon points="617,453 645,495 982,495 1010,453"/>
    <rect x="1010" y="205" width="145" height="248"/>
  </svg>

  <div class="panel panel--front-a">
    <p class="wordmark-bg">VELISA</p>
    <div class="waves" role="img" aria-label="Stylized blue ocean waves"></div>
    <div class="brand"><span class="brand__dot"></span>Velisa</div>
  </div>
  <div class="panel panel--bottom"><p class="name-plate">VELISA</p></div>

  <div class="panel panel--side-b">
    <div class="spec-box spec-box--code"><div class="spec-box__label">CODE/</div></div>
    <div class="spec-box spec-box--size"><div class="spec-box__label">SIZE/</div></div>
    <div class="care-icons">
      <svg class="care-icon" viewBox="0 0 20 20" aria-label="Keep dry"><rect x="1" y="1" width="18" height="18" rx="3"/><path class="glyph" d="M10 4 C13 8 14 10 14 12 A4 4 0 0 1 6 12 C6 10 7 8 10 4Z"/><path class="line" d="M5 15 L15 5"/></svg>
      <svg class="care-icon" viewBox="0 0 20 20" aria-label="Handle with care"><rect x="1" y="1" width="18" height="18" rx="3"/><circle class="glyph" cx="10" cy="7" r="2.5"/><path class="line" d="M4 10 Q5 15 10 15 Q15 15 16 10"/></svg>
      <svg class="care-icon" viewBox="0 0 20 20" aria-label="Maximum stack 10 cartons"><rect x="1" y="1" width="18" height="18" rx="3"/><text x="10" y="11" text-anchor="middle">10</text><path class="line" d="M5 13.5 H15 M5 16 H15"/></svg>
      <svg class="care-icon" viewBox="0 0 20 20" aria-label="Recyclable"><rect x="1" y="1" width="18" height="18" rx="3"/><path class="line" d="M10 4.5 L6 11 M7.5 14.5 H14 M15 11 L12 6"/><path class="glyph" d="M10 4 L12.5 5.5 L10.5 7Z M6 15 L5 12.5 L7.5 13Z M15.5 12 L13.5 14.5 L13 12Z"/></svg>
    </div>
  </div>

  <div class="panel panel--top"><p class="name-plate name-plate--flipped">VELISA</p></div>
  <div class="panel panel--front-c">
    <p class="wordmark-bg">VELISA</p>
    <div class="waves" role="img" aria-label="Stylized blue ocean waves"></div>
    <div class="brand"><span class="brand__dot"></span>Velisa</div>
  </div>

  <div class="panel panel--side-d">
    <div class="spec-box spec-box--code"><div class="spec-box__label">CODE/</div></div>
    <div class="spec-box spec-box--size"><div class="spec-box__label">SIZE/</div></div>
    <div class="care-icons">
      <svg class="care-icon" viewBox="0 0 20 20" aria-label="Keep dry"><rect x="1" y="1" width="18" height="18" rx="3"/><path class="glyph" d="M10 4 C13 8 14 10 14 12 A4 4 0 0 1 6 12 C6 10 7 8 10 4Z"/><path class="line" d="M5 15 L15 5"/></svg>
      <svg class="care-icon" viewBox="0 0 20 20" aria-label="Handle with care"><rect x="1" y="1" width="18" height="18" rx="3"/><circle class="glyph" cx="10" cy="7" r="2.5"/><path class="line" d="M4 10 Q5 15 10 15 Q15 15 16 10"/></svg>
      <svg class="care-icon" viewBox="0 0 20 20" aria-label="Maximum stack 10 cartons"><rect x="1" y="1" width="18" height="18" rx="3"/><text x="10" y="11" text-anchor="middle">10</text><path class="line" d="M5 13.5 H15 M5 16 H15"/></svg>
      <svg class="care-icon" viewBox="0 0 20 20" aria-label="Recyclable"><rect x="1" y="1" width="18" height="18" rx="3"/><path class="line" d="M10 4.5 L6 11 M7.5 14.5 H14 M15 11 L12 6"/><path class="glyph" d="M10 4 L12.5 5.5 L10.5 7Z M6 15 L5 12.5 L7.5 13Z M15.5 12 L13.5 14.5 L13 12Z"/></svg>
    </div>
  </div>
</section>

</body>
</html>
```